varnoth company need business card, envelope and letterhead design

Check on the attached file wherein you can find our logo and information about the company
Business card will double sided English version and Arabic version

Industry/Entity Type

Business

Requirements
Must have
• include the design also for the letterhead and envelop
Nice to have

```html
<!DOCTYPE html>
<html lang="en">
<head>
<meta charset="utf-8">
<title>Varnoth Stationery</title>
<link rel="stylesheet" href="https://fonts.googleapis.com/css2?family=Open+Sans:wght@400;700;800&family=Cinzel:wght@600&family=Noto+Naskh+Arabic:wght@500&display=swap">
<style>
  :root {
    --stage: #333333;
    --paper: #ffffff;
    --brand-blue: #1878c6;
    --brand-grey: #8c8c8c;
    --ink-blue: #1a6fb8;
    --ink-grey: #7a7a7a;
    --ghost: #f1f3f8;
  }
  * { box-sizing: border-box; margin: 0; padding: 0; }
  html, body { width: 1200px; height: 790px; overflow: hidden; background: var(--stage); }
  body { position: relative; font-family: "Open Sans", Arial, sans-serif; }

  .sheet { position: absolute; background: var(--paper); box-shadow: 3px 4px 8px rgba(0,0,0,.55); overflow: hidden; }

  .wordmark { position: absolute; display: flex; align-items: center; gap: 6px; }
  .wordmark .mark { background: var(--brand-blue); }
  .wordmark .name { font-family: "Open Sans", Arial, sans-serif; font-weight: 800; color: var(--brand-blue); letter-spacing: .06em; text-transform: uppercase; line-height: 1; }
  .wordmark-arabic { position: absolute; font-family: "Noto Naskh Arabic", serif; color: var(--brand-grey); line-height: 1; }
  .on-blue .mark { background: #fff; }
  .on-blue .name { color: #fff; }
  .on-blue + .wordmark-arabic, .wordmark-arabic.light { color: #cfe2f4; }

  .ghost-mark { position: absolute; background: var(--ghost); }

  .contact { position: absolute; color: var(--ink-blue); font-weight: 700; line-height: 1.45; }
  .contact-icons { position: absolute; color: var(--ink-grey); font-weight: 700; line-height: 1.9; }
  .contact-icons li { list-style: none; display: flex; align-items: center; gap: 4px; }
  .dot { display: inline-block; border-radius: 50%; background: var(--brand-blue); }
  .divider { position: absolute; width: 1px; background: var(--ink-grey); }

  .footer-band { position: absolute; left: 0; right: 0; bottom: 0; }
  .tab { position: absolute; background: var(--brand-blue); }

  /* letterhead */
  .letterhead { left: 78px; top: 68px; width: 458px; height: 646px; }
  /* envelope front */
  .envelope-front { left: 595px; top: 68px; width: 527px; height: 229px; }
  /* envelope back */
  .envelope-back { left: 595px; top: 336px; width: 527px; height: 228px; }
  .flap { position: absolute; left: 0; top: 0; }

  /* business cards */
  .card { position: absolute; width: 193px; height: 112px; border-radius: 7px; overflow: hidden; box-shadow: 2px 3px 6px rgba(0,0,0,.5); }
  .card-front { left: 654px; top: 605px; background: var(--paper); }
  .card-back { left: 878px; top: 605px; background: var(--brand-blue); }
  .card-person { position: absolute; left: 0; right: 0; top: 53px; text-align: center; font-family: "Cinzel", Georgia, serif; font-weight: 600; font-size: 7.6px; color: var(--ink-blue); }
  .card-role { display: block; font-size: 5px; color: var(--ink-grey); margin-top: 0; }
  .card-strip { position: absolute; left: 0; right: 0; top: 676px; }
  .card-lower { position: absolute; left: 0; right: 0; top: 73px; bottom: 0; background: var(--brand-blue); border-top: 2px solid var(--brand-grey); }
  .card-lower .contact, .card-lower .contact-icons { color: #fff; }
  .card-lower .dot { background: #fff; }
  .card-lower .divider { background: #fff; }

  .signature-mark { left: 1058px; top: 740px; }
</style>
</head>
<body>

<!-- Letterhead -->
<section class="sheet letterhead" aria-label="Letterhead">
  <div class="wordmark" style="left:56px; top:42px;">
    <span class="mark" style="width:22px;height:22px;"></span>
    <span class="name" style="font-size:24px;">Varnoth</span>
  </div>
  <div class="wordmark-arabic" style="left:148px; top:70px; font-size:15px;">فارنوث</div>

  <span class="divider" style="left:300px; top:34px; height:75px;"></span>
  <p class="contact" style="left:314px; top:48px; font-size:6.6px;">Al Noor Street<br>Al Waha<br>P.O. Box 4521-11830</p>
  <ul class="contact-icons" style="left:314px; top:77px; font-size:6.4px;">
    <li><span class="dot" style="width:6px;height:6px;"></span>+966 555 318 204</li>
    <li><span class="dot" style="width:6px;height:6px;"></span>varnoth.sa@mail.com</li>
  </ul>
  <span class="tab" style="right:0; top:54px; width:5px; height:32px;"></span>

  <div class="ghost-mark" role="img" aria-label="Faint brand mark watermark" style="left:74px; top:170px; width:316px; height:316px;"></div>

  <svg class="footer-band" width="458" height="8" viewBox="0 0 458 8" aria-hidden="true">
    <polygon points="0,0 266,0 248,8 0,8" fill="var(--brand-blue)"/>
    <polygon points="270,0 458,0 458,8 252,8" fill="var(--brand-grey)"/>
  </svg>
</section>

<!-- Envelope front -->
<section class="sheet envelope-front" aria-label="Envelope front">
  <span class="tab" style="left:0; top:38px; width:6px; height:34px;"></span>
  <div class="wordmark" style="left:35px; top:36px;">
    <span class="mark" style="width:16px;height:16px;"></span>
    <span class="name" style="font-size:17px;">Varnoth</span>
  </div>
  <div class="wordmark-arabic" style="left:100px; top:56px; font-size:11px;">فارنوث</div>

  <div class="ghost-mark" role="img" aria-label="Faint brand mark watermark" style="left:313px; top:16px; width:196px; height:196px;"></div>

  <p class="contact" style="left:31px; top:179px; font-size:5.2px;">Al Noor Street<br>Al Waha - P.O. Box 4521-11830</p>
  <span class="divider" style="left:119px; top:176px; height:22px;"></span>
  <ul class="contact-icons" style="left:124px; top:177px; font-size:5.2px; line-height:1.8;">
    <li><span class="dot" style="width:5px;height:5px;"></span>+966 555 318 204</li>
    <li><span class="dot" style="width:5px;height:5px;"></span>varnoth.sa@mail.com</li>
  </ul>

  <svg class="footer-band" width="527" height="9" viewBox="0 0 527 9" aria-hidden="true">
    <polygon points="0,0 250,0 238,9 0,9" fill="var(--brand-blue)"/>
    <polygon points="262,0 527,0 527,9 246,9" fill="var(--brand-grey)"/>
  </svg>
</section>

<!-- Envelope back -->
<section class="sheet envelope-back" aria-label="Envelope back">
  <svg class="flap" width="527" height="76" viewBox="0 0 527 76" aria-hidden="true">
    <path d="M0,0 H527 L507,70 Q505,76 499,76 H28 Q22,76 20,70 Z" fill="var(--brand-blue)"/>
  </svg>
  <div class="wordmark on-blue" style="left:212px; top:33px;">
    <span class="mark" style="width:11px;height:11px;"></span>
    <span class="name" style="font-size:11.5px;">Varnoth</span>
  </div>
  <div class="wordmark-arabic light" style="left:252px; top:46px; font-size:8px;">فارنوث</div>

  <div class="ghost-mark" role="img" aria-label="Faint brand mark watermark" style="left:17px; top:88px; width:122px; height:124px;"></div>
</section>

<!-- Business card front -->
<section class="card card-front" aria-label="Business card front">
  <div class="wordmark" style="left:42px; top:15px;">
    <span class="mark" style="width:12px;height:12px;"></span>
    <span class="name" style="font-size:12.5px;">Varnoth</span>
  </div>
  <div class="wordmark-arabic" style="left:90px; top:30px; font-size:8px;">فارنوث</div>
  <p class="card-person">Faisal Bin Omar Al Rashidi<span class="card-role">General Manager</span></p>
  <div class="card-lower">
    <p class="contact" style="left:22px; top:7px; font-size:4.6px;">Al Noor Street.<br>Al Waha,<br>P.O. Box 4521-11830</p>
    <span class="divider" style="left:95px; top:5px; height:28px;"></span>
    <ul class="contact-icons" style="left:105px; top:7px; font-size:4.6px; line-height:2;">
      <li><span class="dot" style="width:4px;height:4px;"></span>+966 555 318 204</li>
      <li><span class="dot" style="width:4px;height:4px;"></span>varnoth.sa@mail.com</li>
    </ul>
  </div>
</section>

<!-- Business card back -->
<section class="card card-back" aria-label="Business card back">
  <div class="wordmark on-blue" style="left:43px; top:48px;">
    <span class="mark" style="width:13px;height:13px;"></span>
    <span class="name" style="font-size:13px;">Varnoth</span>
  </div>
  <div class="wordmark-arabic light" style="left:94px; top:64px; font-size:8px;">فارنوث</div>
</section>

<!-- Brand sign-off -->
<div class="wordmark signature-mark">
  <span class="mark" style="width:14px;height:14px;"></span>
  <span class="name" style="font-size:14px;">Varnoth</span>
</div>
<div class="wordmark-arabic" style="left:1112px; top:757px; font-size:9px;">فارنوث</div>

</body>
</html>
```